Project Title:
Dental Implant Overdenture Flyer (Retirement Village Target)
Objective:
Create a clean, trustworthy, and reassuring flyer aimed at older adults (60–85 years old) who struggle with loose dentures. The goal is to educate them about implant-retained “clip-on” dentures and encourage them to book a consultation.
Tone & Feel:
Warm, caring, non-intimidating
Premium but not “salesy”
Medical but easy to understand
Focus on improving quality of life (confidence, eating, comfort)
Target Audience:
Retirees / pensioners
Existing denture wearers
People frustrated with loose or uncomfortable dentures
Key Message:
“You don’t have to live with loose dentures anymore.”
Design Style:
Clean, minimal, modern
Soft colours (blues, greens, warm neutrals)
Easy-to-read large font
High contrast for older eyes
Avoid clutter
Imagery Suggestions:
Smiling older adults (natural, not stocky/overly staged)
Before/after lifestyle (eating, laughing, socialising)
Simple diagram showing denture clipping onto implants
Avoid graphic surgical images
Layout Suggestions:
A5 or DL flyer
Clear sections with headings
Icons for benefits
Strong call-to-action at bottom
HEADLINE (big and bold)
Tired of Loose Dentures?
Discover Secure “Clip-On” Teeth
🔹 PROBLEM SECTION
Do your dentures:
Slip or move when eating?
Make it hard to chew certain foods?
Feel uncomfortable or loose?
Affect your confidence when speaking or smiling?
You’re not alone — and there is a better solution.
🔹 SOLUTION SECTION
Implant-Retained “Clip-On” Dentures
We can secure your denture using just 2 dental implants, allowing your teeth to:
✔ Stay firmly in place
✔ Improve your ability to eat
✔ Feel more comfortable
✔ Boost your confidence
🔹 SIMPLE EXPLANATION (very important)
Small titanium implants are gently placed in the jaw.
Your denture then clips securely onto them, stopping movement.
🔹 PRICE SECTION (highlight this clearly)
$12,000
Includes:
2 dental implants
A brand new custom overdenture
Does not include sedation or extractions (if needed)
🔹 SEDATION
Sedation is available for comfort.
If you hold a pensioner card, you may receive a significant Vantacor rebate, often resulting in minimal out-of-pocket costs for sedation.
🔹 TRUST / REASSURANCE
Experienced implant clinician
Gentle, patient-focused care
Modern technology and techniques
🔹 CALL TO ACTION (VERY IMPORTANT)
Book a Free Consultation
📞 Call: 08 9351 4276
🌐 Visit: www.bravonclinic.com.au
📍 Located near Tallowmere shopping centre
🔹 OPTIONAL TAGLINE
Eat Better. Feel Better. Smile with Confidence Again.
Please include some photos to illustrate what a clip on denture looks like with two implants.

```html
<!DOCTYPE html>
<html lang="en">
<head>
<meta charset="utf-8">
<title>Clip-On Dentures Flyer</title>
<link href="https://fonts.googleapis.com/css2?family=Roboto:wght@400;500;700;900&display=swap" rel="stylesheet">
<style>
  :root{
    --navy:#1b2a3d;
    --ink:#161a1f;
    --paper:#f3f4f3;
    --sky:#b9d3e6;
    --sky-deep:#8fb6d6;
    --mint:#cfe8da;
    --tab-top:#86aed3;
    --tab-bottom:#b7dcc6;
    --frame:#9fb4c8;
  }
  *{margin:0;padding:0;box-sizing:border-box}
  html,body{width:842px;height:1200px;overflow:hidden;background:var(--paper)}
  body{font-family:"Roboto",Arial,sans-serif;color:var(--ink)}
  .flyer{
    position:relative;width:842px;height:1200px;overflow:hidden;
    background:
      radial-gradient(ellipse 520px 420px at 100% 0%, var(--sky) 0%, rgba(185,211,230,0) 70%),
      radial-gradient(ellipse 600px 520px at 100% 100%, var(--mint) 0%, rgba(207,232,218,0) 72%),
      radial-gradient(ellipse 420px 300px at 0% 0%, #d6e4ee 0%, rgba(214,228,238,0) 70%),
      var(--paper);
  }
  .tab{position:absolute;left:0;width:34px;border-radius:0 30px 30px 0}
  .tab--top{top:60px;height:170px;background:linear-gradient(180deg,var(--tab-top),var(--tab-bottom))}
  .tab--bottom{top:830px;height:220px;background:linear-gradient(180deg,var(--tab-top),var(--tab-bottom))}

  .headline{position:absolute;left:62px;top:52px;font-weight:700;font-size:64px;line-height:1.08;color:var(--navy);letter-spacing:-0.5px}
  .subhead{position:absolute;left:62px;top:194px;font-size:32px;color:var(--ink)}

  .section-title{position:absolute;left:62px;font-weight:700;font-size:34px;color:var(--ink)}
  .bullets{position:absolute;left:70px;list-style:none;font-size:27px;line-height:33px}
  .bullets li{position:relative;padding-left:24px}
  .bullets li::before{content:"";position:absolute;left:2px;top:13px;width:9px;height:9px;border-radius:50%;background:var(--ink)}
  .body-text{position:absolute;left:62px;font-size:27px;line-height:33px}
  .body-text strong{font-weight:700}

  .photo-dining{position:absolute;left:494px;top:50px;width:336px;height:336px;border-radius:50%;
    background:radial-gradient(circle at 45% 40%,#efe5d8 0%,#c9b8a2 55%,#9c8a74 100%)}
  .photo-smile{position:absolute;left:570px;top:454px;width:230px;height:197px;border-radius:20px;
    background:radial-gradient(circle at 40% 40%,#ead7c8 0%,#c9ab94 60%,#a98d7b 100%)}
  .diagram{position:absolute;left:570px;top:689px;width:230px;height:177px;border-radius:16px;border:2px solid var(--frame);
    background:linear-gradient(180deg,#ffffff 0%,#f4dede 55%,#e7a9a9 100%)}

  .cta{position:absolute;left:62px;top:1052px;font-weight:700;font-size:48px;color:var(--ink)}
  .contact{position:absolute;left:62px;top:1106px;font-size:17.5px;font-weight:500;white-space:nowrap}
  .contact .sep{margin:0 7px}
  .location{position:absolute;left:446px;top:1130px;font-size:17.5px;font-weight:500;display:flex;align-items:center;gap:4px}
  .location svg{width:18px;height:18px}
  .tagline{position:absolute;left:0;right:0;top:1158px;text-align:center;font-weight:700;font-size:23px}
</style>
</head>
<body>
<main class="flyer">
  <div class="tab tab--top"></div>
  <div class="tab tab--bottom"></div>

  <h1 class="headline">Secure,<br>Clip-On Teeth.</h1>
  <p class="subhead">No More Loose Dentures.</p>

  <div class="photo-dining" role="img" aria-label="Smiling older couple enjoying a meal together at a kitchen table"></div>

  <h2 class="section-title" style="top:262px">The Problem</h2>
  <ul class="bullets" style="top:305px">
    <li>Slip or move when eating</li>
    <li>Hard to chew foods</li>
    <li>Uncomfortable and loose</li>
    <li>Lowers confidence</li>
  </ul>

  <h2 class="section-title" style="top:464px">Our Solution</h2>
  <ul class="bullets" style="top:507px">
    <li>Clip-On Dentures are firm</li>
    <li>Eat foods easily</li>
    <li>Increased comfort</li>
    <li>Smile confidently</li>
  </ul>
  <div class="photo-smile" role="img" aria-label="Older woman laughing with a confident smile"></div>

  <h2 class="section-title" style="top:668px">Simple Process</h2>
  <p class="body-text" style="top:710px">Small titanium implants gently connect<br>your custom dentures to your jaw,<br>stopping all movement.</p>
  <div class="diagram" role="img" aria-label="Diagram of a denture clipping onto two implants in the lower jaw"></div>

  <h2 class="section-title" style="top:836px">Pricing &amp; Rebates</h2>
  <p class="body-text" style="top:878px"><strong>$12,000</strong> for 2 implants and overdenture.<br>Sedation available.</p>
  <p class="body-text" style="top:955px">Pensioners may receive significant<br>Vantacor rebates.</p>

  <h2 class="cta">Call Us Now</h2>
  <p class="contact">Book a Free Consultation<span class="sep">|</span>Call: 08 9351 4276<span class="sep">|</span>Visit: www.bravonclinic.com.au</p>
  <p class="location">
    <svg viewBox="0 0 18 18" aria-hidden="true"><circle cx="9" cy="9" r="8.5" fill="#5d6f80"/><path d="M6 4.5l1.8 0 .8 2.3-1.1.9a6 6 0 0 0 2.8 2.8l.9-1.1 2.3.8v1.8a1.2 1.2 0 0 1-1.3 1.2A8 8 0 0 1 4.8 5.8 1.2 1.2 0 0 1 6 4.5z" fill="#fff"/></svg>
    <svg viewBox="0 0 18 18" aria-hidden="true"><circle cx="9" cy="9" r="8.5" fill="#5d6f80"/><path d="M9 3.6a3.4 3.4 0 0 0-3.4 3.4c0 2.5 3.4 6.4 3.4 6.4s3.4-3.9 3.4-6.4A3.4 3.4 0 0 0 9 3.6zm0 4.7a1.3 1.3 0 1 1 0-2.6 1.3 1.3 0 0 1 0 2.6z" fill="#fff"/></svg>
    Located near Tallowmere shopping centre
  </p>
  <p class="tagline">Eat, Feel, and Smile with Confidence.</p>
</main>
</body>
</html>
```